Become an EMT and Serve your community!

We are looking to design a postcard that will be mailed to surrounding communities that notifies them of our upcoming EMT class with an emphasis of serving their community. We are looking for a design that grabs peoples attention and motivates them to sign up and serve their community. Our primary colors are red and blue. We would like to incorporate the Institute logo as well as one or two photos. We do have more photos available upon request. Our Institute website is www.halvorsenacademy.net for more material. It is important that the postcard meets mailing guidelines.

Target Market(s)

Local community members

Industry/Entity Type

Education

Font styles to use
Sans Serif

Colors
f04a50
3176b5
0255a3
eaf1f7

Requirements
Must have
• Dates
Prices
Contact info
Look interesting
Convey the message of “Serving your Community”
Nice to have
• Clear information
Concise
Incorporate an action shot
Should not have
• Generic EMS logos

```html
<!DOCTYPE html>
<html lang="en">
<head>
<meta charset="utf-8">
<title>2020 Summer EMT Class Postcard</title>
<link href="https://fonts.googleapis.com/css2?family=Oswald:wght@700&family=Lato:wght@400;700&display=swap" rel="stylesheet">
<style>
  :root {
    --stage: #3d3d3d;
    --red: #f04a50;
    --blue: #0255a3;
    --navy: #2a2c78;
    --white: #ffffff;
    --ink: #1c1c1c;
    --photo-a: #c9b79a;
    --photo-b: #4d6fb0;
    --photo-c: #7a6c66;
    --photo-d: #c23a3c;
  }
  * { margin: 0; padding: 0; box-sizing: border-box; }
  html, body { width: 1200px; height: 1200px; overflow: hidden; }
  body { background: var(--stage); position: relative; font-family: "Lato", sans-serif; }

  .card { position: absolute; background: var(--white); overflow: hidden; }

  /* Front */
  .card-front { left: 131px; top: 137px; width: 586px; height: 454px; }
  .front-art { position: absolute; left: 0; top: 0; }
  .title { position: absolute; left: 15px; top: 30px; font-family: "Oswald", sans-serif; font-weight: 700; font-size: 50px; line-height: 54px; letter-spacing: -0.5px; }
  .title .accent { color: var(--red); display: block; }
  .title .main { color: var(--blue); display: block; }
  .tag { position: absolute; background: var(--blue); color: var(--white); font-weight: 700; font-size: 13px; line-height: 20px; padding: 0 10px 0 17px; border-radius: 0 10px 10px 0; }
  .tag-when { left: 0; top: 150px; }
  .schedule { position: absolute; left: 15px; top: 178px; font-size: 15.5px; line-height: 19px; color: var(--ink); }
  .schedule .dates { color: var(--red); font-weight: 700; }
  .lab-note { position: absolute; left: 15px; top: 220px; width: 250px; font-size: 12.5px; line-height: 16px; color: var(--ink); }
  .lab-note b { color: var(--navy); }
  .brand { position: absolute; left: 14px; top: 300px; display: flex; align-items: center; gap: 6px; }
  .brand-dot { width: 14px; height: 14px; border-radius: 50%; background: var(--blue); }
  .brand-name { font-weight: 700; font-size: 12px; color: var(--blue); width: 80px; line-height: 14px; }
  .weekend { position: absolute; left: 0; top: 343px; width: 586px; height: 97px; background: var(--navy); border-top: 5px solid var(--red); color: var(--white); text-align: center; }
  .weekend p { font-size: 16.5px; line-height: 21px; }
  .weekend p:first-child { margin-top: 12px; }
  .weekend-hours { display: inline-block; margin-top: 6px; background: var(--red); border-radius: 11px; padding: 0 14px; font-weight: 700; font-size: 16px; line-height: 22px; }

  /* Back */
  .card-back { left: 513px; top: 641px; width: 577px; height: 447px; }
  .back-art { position: absolute; left: 0; top: 0; }
  .tag-tuition { left: 0; top: 250px; font-size: 18px; line-height: 22px; padding: 0 14px; background: var(--navy); border-radius: 0 11px 11px 0; }
  .fees { position: absolute; left: 17px; top: 276px; list-style: none; color: var(--white); font-size: 13.5px; line-height: 20px; }
  .fees li { display: flex; align-items: center; gap: 4px; }
  .fees svg { flex: none; }
  .pitch { position: absolute; left: 14px; top: 318px; width: 292px; color: var(--white); font-size: 12.2px; line-height: 15.5px; }
  .site { position: absolute; left: 66px; top: 414px; display: flex; align-items: center; gap: 7px; color: var(--white); font-size: 13px; letter-spacing: 0.3px; }
  .stamp-box { position: absolute; left: 522px; top: 16px; width: 41px; height: 40px; border: 1px solid #888; background: #f2f2f2; }
  .address-line { position: absolute; left: 384px; width: 170px; height: 2px; background: var(--ink); }
</style>
</head>
<body>

<section class="card card-front">
  <svg class="front-art" width="586" height="347" viewBox="0 0 586 347">
    <defs>
      <linearGradient id="trainingTones" x1="0" y1="0" x2="1" y2="1">
        <stop offset="0" stop-color="var(--photo-a)"/>
        <stop offset="0.55" stop-color="var(--photo-b)"/>
        <stop offset="1" stop-color="#2f3548"/>
      </linearGradient>
    </defs>
    <path role="img" aria-label="Photo: EMT students practising airway care on a training manikin" d="M333 0 L586 0 L586 347 L110 347 C310 290 340 170 333 0 Z" fill="url(#trainingTones)"/>
    <path d="M333 0 C340 170 310 290 110 347" fill="none" stroke="var(--red)" stroke-width="8"/>
  </svg>

  <h1 class="title"><span class="accent">2020 SUMMER</span><span class="main">EMT CLASS</span></h1>
  <span class="tag tag-when">When</span>
  <p class="schedule">Monday, Tuesday, Wednesday from<br><span class="dates">May 26th through August 17th.</span></p>
  <p class="lab-note"><b>Wednesdays :</b> Students will need to sign up for either a 4:00 p - 7:00 p lab section, or a 7:00p-10:0p lab section.</p>
  <div class="brand"><span class="brand-dot"></span><span class="brand-name">Halvorsen Institute</span></div>

  <div class="weekend">
    <p>There will be one required <b>Sat/Sun weekend</b> held for all students.</p>
    <p>This will take place on <b>June 13th &amp; 14th.</b></p>
    <span class="weekend-hours">Weekend classes will run from&nbsp; 8:00 am - 8:00 pm.</span>
  </div>
</section>

<section class="card card-back">
  <svg class="back-art" width="577" height="447" viewBox="0 0 577 447">
    <defs>
      <linearGradient id="ambulanceTones" x1="0" y1="0" x2="0" y2="1">
        <stop offset="0" stop-color="var(--photo-c)"/>
        <stop offset="0.6" stop-color="var(--photo-d)"/>
        <stop offset="1" stop-color="var(--red)"/>
      </linearGradient>
      <radialGradient id="insetTones">
        <stop offset="0" stop-color="#a8856a"/>
        <stop offset="1" stop-color="#2d2a2a"/>
      </radialGradient>
    </defs>
    <rect role="img" aria-label="Photo: paramedics in red jackets caring for a patient inside an ambulance" x="0" y="0" width="420" height="250" fill="url(#ambulanceTones)"/>
    <rect x="0" y="243" width="420" height="156" fill="var(--red)"/>
    <rect x="0" y="399" width="420" height="8" fill="var(--white)"/>
    <rect x="0" y="407" width="420" height="40" fill="var(--navy)"/>
    <path d="M395 0 C340 90 305 190 312 260 C318 330 340 400 372 447 L577 447 L577 0 Z" fill="var(--navy)"/>
    <path d="M395 0 C340 90 305 190 312 260 C318 330 340 400 372 447" fill="none" stroke="var(--white)" stroke-width="5"/>
    <path d="M412 0 C355 90 322 190 330 260 C338 330 370 400 410 447 L577 447 L577 0 Z" fill="var(--white)"/>
    <circle cx="319" cy="249" r="44" fill="var(--navy)"/>
    <circle role="img" aria-label="Photo: hands giving chest compressions during CPR practice" cx="319" cy="249" r="38" fill="url(#insetTones)" stroke="var(--white)" stroke-width="2"/>
  </svg>

  <span class="tag tag-tuition">Tuition</span>
  <ul class="fees">
    <li><svg width="11" height="11" viewBox="0 0 11 11"><circle cx="5.5" cy="5.5" r="4.5" fill="none" stroke="#fff" stroke-width="1"/><path d="M3 5.6 L4.9 7.4 L8 3.9" fill="none" stroke="#fff" stroke-width="1.2"/></svg><span><b>$1000 EMT</b> (without CPR).</span></li>
    <li><svg width="11" height="11" viewBox="0 0 11 11"><circle cx="5.5" cy="5.5" r="4.5" fill="none" stroke="#fff" stroke-width="1"/><path d="M3 5.6 L4.9 7.4 L8 3.9" fill="none" stroke="#fff" stroke-width="1.2"/></svg><span><b>$250 DEPOSIT</b> is due at time of registration.</span></li>
  </ul>
  <p class="pitch">Serve your community and become an Emergency Medical Technician. As a student you will have access to cutting edge training equipment, experienced instructors, and be able to train on a 911 Ambulance through Halvorsen EMS.</p>
  <div class="site">
    <svg width="15" height="15" viewBox="0 0 16 16" fill="none" stroke="#fff" stroke-width="1.1"><circle cx="8" cy="8" r="6.5"/><ellipse cx="8" cy="8" rx="3" ry="6.5"/><path d="M1.5 8 H14.5 M2.5 4.7 H13.5 M2.5 11.3 H13.5"/></svg>
    <span>www.halvorsenacademy.net</span>
  </div>

  <div class="stamp-box"></div>
  <div class="address-line" style="top:237px"></div>
  <div class="address-line" style="top:266px"></div>
  <div class="address-line" style="top:295px"></div>
</section>

</body>
</html>
```